Paint Factory Needs Bucket Designs

I have paint factory and I want Paint buckets designs. The buckets should be the below sizes:

1 ltr
4 ltrs
10 ltrs
20 ltrs

```html
<!DOCTYPE html>
<html lang="en">
<head>
<meta charset="utf-8">
<title>Velmora Paints – 10 ltrs Bucket Label</title>
<link rel="stylesheet" href="https://fonts.googleapis.com/css2?family=Yeseva+One&family=Open+Sans:wght@400;700&display=swap">
<style>
  :root{
    --stage:#b3b1b2;
    --navy:#1a3a8c;
    --white:#ffffff;
    --sky:#2fa6e6;
    --red:#e3101b;
    --gold:#ffd21a;
    --amber:#f5a21b;
    --orange:#ef7d12;
    --ink:#2a2a2a;
  }
  *{margin:0;padding:0;box-sizing:border-box}
  html,body{width:1200px;height:660px;overflow:hidden}
  body{background:var(--stage);position:relative;font-family:"Open Sans",sans-serif}
  .label{position:absolute;left:53px;top:172px;width:1094px;height:315px;overflow:hidden;background:var(--navy)}
  .label-shapes{position:absolute;inset:0}
  .display{font-family:"Yeseva One",serif;font-weight:400}
  .headline{position:absolute;background:linear-gradient(180deg,var(--gold),var(--amber));-webkit-background-clip:text;background-clip:text;color:transparent;white-space:nowrap}
  .directions-title{left:34px;top:30px;font-size:30px}
  .brand-title{left:0;width:1080px;text-align:center;top:36px;font-size:31px}
  .product-sub{position:absolute;left:0;width:1080px;text-align:center;top:76px;color:var(--white);font-size:19px;line-height:21px}
  .ribbon-art{position:absolute;left:360px;top:128px;width:330px;height:138px;
    background:linear-gradient(90deg,#3a4fc4 0%,#2fa6e6 26%,#2cc39a 44%,#8fd04a 56%,#f39a1f 74%,#e3401b 100%);
    -webkit-mask-image:radial-gradient(ellipse at center,#000 45%,transparent 72%);
    mask-image:radial-gradient(ellipse at center,#000 45%,transparent 72%)}
  .volume{position:absolute;left:0;width:1080px;text-align:center;top:266px;font-size:23px;color:var(--orange)}
  .col{position:absolute;top:136px;width:148px}
  .col-left{left:34px}
  .col-right{left:195px}
  .divider{position:absolute;left:181px;top:138px;width:2px;height:152px;background:var(--orange)}
  .step{margin-bottom:12px}
  .step-title{font-family:"Yeseva One",serif;color:var(--orange);font-size:15px;line-height:20px}
  .step-text{font-size:8.6px;line-height:12.6px;color:var(--ink)}
  .maker-title{position:absolute;left:755px;width:290px;text-align:center;top:30px;font-size:29px}
  .maker-rule{position:absolute;left:755px;top:75px;width:290px;height:3px;background:var(--gold)}
  .maker-name{position:absolute;left:755px;width:290px;text-align:center;top:84px;color:var(--white);font-size:16.5px;line-height:23px}
  .maker-address{position:absolute;left:782px;top:131px;color:var(--white);font-size:12.5px;display:flex;align-items:center;gap:6px;white-space:nowrap}
  .details{position:absolute;left:775px;width:255px;text-align:center;top:220px}
  .detail-row{font-family:"Yeseva One",serif;color:var(--orange);font-size:15px;line-height:20px}
  .detail-row b{font-family:"Open Sans",sans-serif;font-weight:700;color:#111;font-size:14px;margin-left:4px}
  .support-title{font-family:"Yeseva One",serif;color:var(--orange);font-size:15px;line-height:18px}
  .support-text{font-size:9px;line-height:13px;color:var(--ink)}
</style>
</head>
<body>
  <main class="label">
    <svg class="label-shapes" width="1094" height="315" viewBox="0 0 1094 315" aria-hidden="true">
      <defs>
        <radialGradient id="centerGlow" cx="0.5" cy="0.4" r="0.6">
          <stop offset="0" stop-color="#2a55b8"/>
          <stop offset="1" stop-color="#1a3a8c"/>
        </radialGradient>
      </defs>
      <rect x="360" y="0" width="362" height="315" fill="url(#centerGlow)"/>
      <path d="M0,140 C90,92 220,76 340,118 L345,128 C220,88 90,104 0,152 Z" fill="var(--sky)"/>
      <path d="M640,190 C780,172 960,150 1094,92 L1094,170 C980,182 850,192 700,205 Z" fill="var(--red)"/>
      <path d="M0,150 C90,100 220,86 340,126 C420,160 470,230 525,232 C590,234 640,205 700,205 C850,192 980,182 1094,170 L1094,315 L0,315 Z" fill="var(--white)"/>
    </svg>

    <div class="ribbon-art" role="img" aria-label="Flowing multicolour paint brush stroke ribbon in blue, teal, green, orange and red"></div>

    <h2 class="display headline directions-title">Directions For Use</h2>

    <h1 class="display headline brand-title">Velmora Paints</h1>
    <p class="display product-sub">Rapid Interior<br>Emulsion</p>
    <p class="display volume">10 ltrs</p>

    <section class="col col-left">
      <div class="step">
        <h3 class="step-title">Cleaning:</h3>
        <p class="step-text">Surface should be free from any loose paint, dust or grease. Growth of Fungus &amp; Algae should be removed using wire brush &amp; water.</p>
      </div>
      <div class="step">
        <h3 class="step-title">Priming:</h3>
        <p class="step-text">Apply one coat of Velmora Paints wall primer by thinning 1:1 primer &amp; water. Allow to dry for 4 hours.</p>
      </div>
    </section>
    <div class="divider"></div>
    <section class="col col-right">
      <div class="step">
        <h3 class="step-title">Filling:</h3>
        <p class="step-text">Dents &amp; Holes must be filled using Velmora Paints wall putty. Allow to dry for 4 hours.</p>
      </div>
      <div class="step">
        <h3 class="step-title">Finish Coats:</h3>
        <p class="step-text">Apply two or three coats of Velmora Paints exterior or interior emulsion paint by thinning 2:1 paint &amp; water with an interval of 4 - 6 hours.</p>
      </div>
    </section>

    <h2 class="display headline maker-title">Manufactured by</h2>
    <div class="maker-rule"></div>
    <p class="display maker-name">Velmora Paints<br>Rapid Interior Emulsion</p>
    <p class="maker-address">
      <svg width="10" height="13" viewBox="0 0 10 13" aria-hidden="true"><path d="M5,0 C2.2,0 0,2.2 0,5 C0,8.5 5,13 5,13 C5,13 10,8.5 10,5 C10,2.2 7.8,0 5,0 Z" fill="var(--gold)"/><circle cx="5" cy="5" r="2" fill="var(--navy)"/></svg>
      B-12 Quarry Lane Ashbridge
    </p>

    <section class="details">
      <p class="detail-row">Mfg. Date: <b>04/2021</b></p>
      <p class="detail-row">MRP: <b>150$</b></p>
      <p class="support-title">For Suggestion &amp; Complaint:</p>
      <p class="support-text">Contact Customer Care Executive: (5550) 123 456</p>
      <p class="support-text">E-mail: info@velmorapaints.example</p>
    </section>
  </main>
</body>
</html>
```